MARLOW CREST WINE LABEL DESIGN PROJECT

We need an elegant wine label design for our new range of wine. We need 3 labels for the range

2015 MARLOW CREST SHIRAZ
2015 MARLOW CREST CABERNET SAUVIGNON
2015 MARLOW CREST CABERNET SHIRAZ

The Size is nominated at 120mm High x 90mm Wide (Front and Back) but we are open to creative expression even if size differs

We are open to any style of label and designer can work on their strengths. it can be modern/classic/old fashion etc

I have attached the marlow crest logo ( the 2 olives) and a set up called wine mandatories which is in no way a design direction just the mandatory info that needs to appear on labels. The wine mandatories is just the information that needs to go on the label it has nothing to do with the design. DO not make designs based on this at all. These labels are for red wine not olive oil.

I have also attached some of the companies current olive oil labels ( TORQUALE AND WANDELLA AND MARLOW CREST so you can see other labels and how this wine product will sit in gift baskets.

Thanks
Tomasz.

Reason: Hello Friends We have decided to extend the deadline to enable more submissions. Many of the designs submitted have images of olives and look like olive oil product. We only need the olive logo to be shown on the label but the rest of the design should be a classic simple red wine label. It is not olive oil or olive product - it is red wine. Please keep simple and stylish Thanks Tomasz

Target Market(s)

35-65

Font styles to use
Serif

Requirements
Must have
• AS per brief
Nice to have
• as per brief
Should not have
• as per brief

```html
<!DOCTYPE html>
<html lang="en">
<head>
<meta charset="utf-8">
<title>Marlow Crest Shiraz Label</title>
<link rel="stylesheet" href="https://fonts.googleapis.com/css2?family=Jost:wght@400;500&family=Libre+Bodoni:wght@700&display=swap">
<style>
  :root {
    --backdrop: #e8e5e2;
    --label-white: #fbfbfb;
    --label-shade: #ecebea;
    --ink: #151515;
    --copper: #c0713a;
    --copper-deep: #9a4f22;
    --copper-light: #e6a06a;
    --mark-grey: #d9d9d9;
  }
  html, body {
    margin: 0;
    padding: 0;
    width: 1200px;
    height: 1000px;
    overflow: hidden;
    background: var(--backdrop);
  }
  .canvas {
    position: relative;
    width: 1200px;
    height: 1000px;
  }
  .label {
    position: absolute;
    left: 370px;
    top: 38px;
    width: 460px;
    height: 925px;
    overflow: hidden;
    background: linear-gradient(100deg, var(--label-white) 0%, #f4f4f4 55%, var(--label-shade) 100%);
    box-shadow: 0 2px 10px rgba(0,0,0,0.08);
  }
  .brand-dot {
    position: absolute;
    left: 130px;
    top: 80px;
    width: 110px;
    height: 110px;
    border-radius: 50%;
    background: var(--mark-grey);
  }
  .brand-name {
    position: absolute;
    left: 48px;
    top: 332px;
    margin: 0;
    font-family: "Jost", sans-serif;
    font-weight: 500;
    font-size: 26px;
    letter-spacing: 0.18em;
    color: var(--ink);
    white-space: nowrap;
  }
  .tagline {
    position: absolute;
    right: 46px;
    top: 378px;
    margin: 0;
    text-align: right;
    font-family: "Jost", sans-serif;
    font-weight: 400;
    font-size: 22px;
    line-height: 30px;
    letter-spacing: 0.2em;
    color: var(--copper);
    text-transform: uppercase;
  }
  .region {
    position: absolute;
    left: 56px;
    top: 652px;
    margin: 0;
    font-family: "Jost", sans-serif;
    font-weight: 500;
    font-size: 22px;
    letter-spacing: 0.12em;
    color: var(--copper);
    text-transform: uppercase;
  }
  .region-rule {
    position: absolute;
    left: 56px;
    top: 684px;
    width: 248px;
    height: 2px;
    background: var(--ink);
  }
  .variety {
    position: absolute;
    left: 56px;
    top: 702px;
    margin: 0;
    font-family: "Libre Bodoni", serif;
    font-weight: 700;
    font-size: 27px;
    letter-spacing: 0.01em;
    color: var(--ink);
  }
  .vintage {
    position: absolute;
    left: 56px;
    top: 748px;
    margin: 0;
    font-family: "Jost", sans-serif;
    font-weight: 400;
    font-size: 17px;
    letter-spacing: 0.04em;
    color: var(--ink);
  }
  .foot-wave {
    position: absolute;
    left: 0;
    bottom: 0;
    width: 460px;
    height: 110px;
  }
</style>
</head>
<body>
<main class="canvas">
  <section class="label" aria-label="Marlow Crest Shiraz front label">
    <div class="brand-dot" aria-hidden="true"></div>
    <h1 class="brand-name">THE MARLOW CREST</h1>
    <p class="tagline">Premium<br>Australian<br>Wine</p>

    <p class="region">Lower Murray</p>
    <div class="region-rule"></div>
    <p class="variety">SHIRAZ</p>
    <p class="vintage">2015</p>

    <svg class="foot-wave" viewBox="0 0 460 110" preserveAspectRatio="none" aria-hidden="true">
      <defs>
        <linearGradient id="copperBand" x1="0" y1="0" x2="1" y2="0">
          <stop offset="0" stop-color="var(--copper-deep)"/>
          <stop offset="0.35" stop-color="var(--copper-light)"/>
          <stop offset="0.7" stop-color="var(--copper)"/>
          <stop offset="1" stop-color="var(--copper-deep)"/>
        </linearGradient>
      </defs>
      <path d="M0 30 C60 10 120 8 190 32 C260 56 330 60 400 48 C430 43 448 44 460 48 L460 110 L0 110 Z" fill="url(#copperBand)" opacity="0.45"/>
      <path d="M0 48 C70 24 130 22 200 46 C270 70 340 74 410 62 C435 58 450 60 460 62 L460 110 L0 110 Z" fill="url(#copperBand)"/>
      <path d="M0 62 C70 40 135 38 205 60 C275 82 345 86 415 76 C438 73 452 74 460 76 L460 110 L0 110 Z" fill="var(--label-white)"/>
      <path d="M0 84 C80 70 150 70 220 86 C290 100 370 102 460 94 L460 110 L0 110 Z" fill="url(#copperBand)"/>
    </svg>
  </section>
</main>
</body>
</html>
```